Automotive eCommerce Business looking for a business card design

Looking for a clean and simple business card design. Our company name is "Harbor Crest Auto" and we are a company specializing in the ecommerce sales of automotive parts, specifically for pick up trucks and large SUVs. Our company colours are red, black, and white.

Feel free to use the logo provided or create a new logo that you seem fit. Looking forward to your creative ideas!

Industry/Entity Type

Automotive

Contact Information for Business Card

We were thinking of a possibly two-sided design featuring just the logo and company name on one side, and personal information on the other side. Single sided designs will be considered as well.

Font styles to use
Serif
Sans Serif
Decorative

Colors
ec1f27
ffffff
000000

Requirements
Must have
• Space for employee's name, title, phone number and email address, along with the company address and website somewhere.

```html
<!DOCTYPE html>
<html lang="en">
<head>
<meta charset="utf-8">
<title>Harbor Crest Auto – Business Card</title>
<link rel="stylesheet" href="https://fonts.googleapis.com/css2?family=Open+Sans:wght@400;600;700&display=swap">
<style>
  :root {
    --red: #c8202d;
    --red-deep: #a9151f;
    --red-light: #d8333f;
    --white: #ffffff;
    --ink: #3a3a3a;
    --ink-soft: #6b6b6b;
    --rule: #d9b3b6;
    --backdrop: #ece9e4;
  }
  * { box-sizing: border-box; margin: 0; padding: 0; }
  html, body {
    width: 1200px; height: 1023px; overflow: hidden;
    background: var(--backdrop);
    font-family: "Open Sans", Arial, sans-serif;
  }
  .card {
    position: absolute;
    width: 600px; height: 343px;
    border-radius: 26px;
    overflow: hidden;
    box-shadow: 0 10px 30px rgba(0,0,0,.12);
  }

  /* Front side */
  .card--front { left: 90px; top: 110px; background: var(--white); }
  .front-band { position: absolute; right: 0; top: 0; width: 180px; height: 343px; }
  .person { position: absolute; left: 48px; top: 52px; }
  .person__name {
    color: var(--red); font-weight: 700; font-size: 25px; letter-spacing: .5px; line-height: 1.1;
  }
  .person__title {
    color: var(--ink); font-size: 14px; letter-spacing: .6px; margin-top: 3px;
  }
  .divider { position: absolute; left: 48px; top: 122px; width: 382px; height: 4px; }
  .divider__accent { position: absolute; left: 0; top: 0; width: 120px; height: 4px; background: var(--red); }
  .divider__line { position: absolute; left: 0; top: 2px; width: 382px; height: 1px; background: var(--red); opacity: .6; }
  .contacts { position: absolute; left: 48px; top: 138px; font-size: 15px; line-height: 1.45; color: var(--ink-soft); }
  .contacts .label { color: var(--red); }
  .contacts .web { color: var(--red); }
  .company { position: absolute; left: 48px; top: 252px; display: flex; align-items: center; gap: 16px; }
  .company__dot { width: 44px; height: 44px; border-radius: 50%; background: var(--red); flex: none; }
  .company__text { font-size: 15px; line-height: 1.35; color: var(--ink-soft); }
  .company__name { color: var(--red); font-weight: 700; font-size: 15px; letter-spacing: .4px; }

  /* Back side */
  .card--back {
    left: 510px; top: 570px;
    background: linear-gradient(135deg, var(--red-light) 0%, var(--red) 45%, var(--red-deep) 100%);
  }
  .back__web {
    position: absolute; left: 40px; top: 34px;
    color: var(--white); font-size: 14px; letter-spacing: 1.5px; opacity: .95;
  }
  .back__brand {
    position: absolute; left: 0; right: 0; top: 50%; transform: translateY(-50%);
    text-align: center; color: var(--white); font-weight: 700; font-size: 38px; letter-spacing: 2px;
  }
</style>
</head>
<body>

<section class="card card--front" aria-label="Business card front">
  <svg class="front-band" viewBox="0 0 180 343" aria-hidden="true">
    <path d="M0 0 Q40 0 40 40 L40 303 Q40 343 0 343 L180 343 L180 0 Z" fill="var(--red)"/>
  </svg>

  <div class="person">
    <p class="person__name">JONATHAN DOE</p>
    <p class="person__title">MANAGING DIRECTOR</p>
  </div>

  <div class="divider">
    <span class="divider__line"></span>
    <span class="divider__accent"></span>
  </div>

  <div class="contacts">
    <p>000-000-000 <span class="label">[Tel]</span></p>
    <p>000-000-000 <span class="label">[Fax]</span></p>
    <p>jdoe@harborcrestauto.com <span class="label">[Email]</span></p>
    <p class="web">www.harborcrestauto.com</p>
  </div>

  <div class="company">
    <span class="company__dot" aria-hidden="true"></span>
    <div class="company__text">
      <p class="company__name">HARBOR CREST AUTO</p>
      <p>Company Street Address #470</p>
      <p>City Name, 12345</p>
    </div>
  </div>
</section>

<section class="card card--back" aria-label="Business card back">
  <p class="back__web">www.harborcrestauto.com</p>
  <p class="back__brand">HARBOR CREST AUTO</p>
</section>

</body>
</html>
```